School Communication Email Template

Looking for a designer to create a couple simple email templates that are matching our brand colors and feel. Attached is the default email template that is currently being sent out. Company details can be shared upon request.

Template is to be used within the booking tool we use (snapshot below) and gmail. Template code is in HTML (see screenshot below).
Updates

Template code for website should be in HTML. Sorry if that created confusion.

Target Market(s)

Parents of kids enrolled in our classes

Industry/Entity Type

Kids sport classes

Font styles to use
Serif

Colors
0054AA
0677BA
7BADD7
CADEEF
E8F1F8
FFF300
FFF600
FEFA6F
FFFEC7
FFFEE8

Requirements
Must have
• Consistency with company brand/colors
Nice to have
• Flexibility to be adjusted as needed

```html
<!DOCTYPE html>
<html lang="en">
<head>
<meta charset="utf-8">
<title>Booking Email</title>
<link href="https://fonts.googleapis.com/css2?family=Ubuntu:wght@300;400;500;700&display=swap" rel="stylesheet">
<style>
  :root {
    --navy: #253f86;
    --ink: #111111;
    --field-text: #6b6b6b;
    --field-border: #e2e2e2;
    --card: #ffffff;
    --sky-top: #041226;
    --sky-bottom: #0b4a78;
    --gold: #8f7a2e;
  }
  * { box-sizing: border-box; margin: 0; padding: 0; }
  html, body { width: 758px; height: 1200px; overflow: hidden; }
  body { font-family: "Ubuntu", sans-serif; }
  .canvas { position: relative; width: 758px; height: 1200px; overflow: hidden; }
  .sky {
    position: absolute; inset: 0;
    background:
      radial-gradient(ellipse 60% 30% at 70% 20%, rgba(143,122,46,0.18), transparent 70%),
      radial-gradient(ellipse 70% 25% at 30% 92%, rgba(143,122,46,0.22), transparent 70%),
      linear-gradient(180deg, var(--sky-top) 0%, #07223f 55%, var(--sky-bottom) 100%);
  }
  .brand-tab {
    position: absolute; left: 311px; top: 0; width: 134px; height: 168px;
    background: var(--card); border-radius: 0 0 67px 67px;
    display: flex; align-items: center; justify-content: center; gap: 5px;
  }
  .brand-dot { width: 9px; height: 9px; border-radius: 50%; background: var(--navy); }
  .brand-name { font-weight: 700; font-size: 17px; color: var(--navy); }
  .card {
    position: absolute; left: 52px; top: 202px; width: 654px; height: 820px;
    background: var(--card); border-radius: 8px;
  }
  .heading {
    position: absolute; left: 0; width: 100%; text-align: center;
    font-weight: 700; font-size: 38px; color: var(--navy); line-height: 1;
  }
  .label {
    position: absolute; left: 33px; font-weight: 500; font-size: 21px;
    color: var(--ink); line-height: 1;
  }
  .field {
    position: absolute; height: 43px; border: 2px solid var(--field-border);
    border-radius: 8px; display: flex; align-items: center; justify-content: space-between;
    padding: 0 14px; font-weight: 300; font-size: 11.5px; color: var(--field-text);
  }
  .field svg { width: 11px; height: 11px; fill: var(--navy); flex: none; }
  .half-left { left: 27px; width: 288px; }
  .half-right { left: 340px; width: 288px; }
  .full { left: 27px; width: 597px; }
</style>
</head>
<body>
<div class="canvas">
  <div class="sky" role="img" aria-label="Starry night sky with a golden ring sweeping around the page"></div>

  <div class="brand-tab">
    <span class="brand-dot"></span>
    <span class="brand-name">Orbit Club</span>
  </div>

  <main class="card">
    <h1 class="heading" style="top:22px">DEAR</h1>
    <div class="field half-left" style="top:79px">Dana
      <svg viewBox="0 0 12 12"><circle cx="6" cy="3.5" r="2.6"/><path d="M1 11.5c0-3 2.2-4.8 5-4.8s5 1.8 5 4.8z"/></svg></div>
    <div class="field half-right" style="top:79px">Whitfield.
      <svg viewBox="0 0 12 12"><circle cx="6" cy="3.5" r="2.6"/><path d="M1 11.5c0-3 2.2-4.8 5-4.8s5 1.8 5 4.8z"/></svg></div>

    <h2 class="heading" style="top:147px">BOOKING</h2>

    <div class="label" style="top:195px">Student:</div>
    <div class="field half-left" style="top:220px">Lena
      <svg viewBox="0 0 12 12"><circle cx="6" cy="3.5" r="2.6"/><path d="M1 11.5c0-3 2.2-4.8 5-4.8s5 1.8 5 4.8z"/></svg></div>
    <div class="field half-right" style="top:220px">Biologist
      <svg viewBox="0 0 12 12"><circle cx="6" cy="3.5" r="2.6"/><path d="M1 11.5c0-3 2.2-4.8 5-4.8s5 1.8 5 4.8z"/></svg></div>

    <div class="label" style="top:281px">Appointment:</div>
    <div class="field full" style="top:306px">Nemo enim ipsam
      <svg viewBox="0 0 12 12"><circle cx="6" cy="3.5" r="2.6"/><path d="M1 11.5c0-3 2.2-4.8 5-4.8s5 1.8 5 4.8z"/></svg></div>

    <div class="label" style="top:363px">Service:</div>
    <div class="field full" style="top:388px">swimming
      <svg viewBox="0 0 12 12" style="fill:none;stroke:#253f86;stroke-width:1.3"><path d="M3.5 5l2.5 2.5L8.5 5"/></svg></div>

    <div class="label" style="top:446px">Start Date:</div>
    <div class="field full" style="top:472px">14/02/2023
      <svg viewBox="0 0 12 12"><path d="M1 2.5h10v9H1zM2.2 4.6v5.7h7.6V4.6z"/><rect x="3" y="1" width="1.2" height="2.5"/><rect x="7.8" y="1" width="1.2" height="2.5"/><rect x="3" y="5.6" width="1.4" height="1.2"/><rect x="5.3" y="5.6" width="1.4" height="1.2"/><rect x="7.6" y="5.6" width="1.4" height="1.2"/><rect x="3" y="7.9" width="1.4" height="1.2"/><rect x="5.3" y="7.9" width="1.4" height="1.2"/></svg></div>

    <div class="label" style="top:527px">End Date:</div>
    <div class="field full" style="top:552px">14/02/2023
      <svg viewBox="0 0 12 12"><path d="M1 2.5h10v9H1zM2.2 4.6v5.7h7.6V4.6z"/><rect x="3" y="1" width="1.2" height="2.5"/><rect x="7.8" y="1" width="1.2" height="2.5"/><rect x="3" y="5.6" width="1.4" height="1.2"/><rect x="5.3" y="5.6" width="1.4" height="1.2"/><rect x="7.6" y="5.6" width="1.4" height="1.2"/><rect x="3" y="7.9" width="1.4" height="1.2"/><rect x="5.3" y="7.9" width="1.4" height="1.2"/></svg></div>

    <div class="label" style="top:613px;left:34px">Start Time:</div>
    <div class="field full" style="top:638px;left:28px">2:30 PM
      <svg viewBox="0 0 12 12" style="fill:none;stroke:#253f86;stroke-width:1.3"><circle cx="6" cy="6" r="4.6"/><path d="M6 3.4V6h2"/></svg></div>

    <div class="label" style="top:699px;left:34px">End Time:</div>
    <div class="field full" style="top:724px;left:28px">05:00 PM
      <svg viewBox="0 0 12 12" style="fill:none;stroke:#253f86;stroke-width:1.3"><circle cx="6" cy="6" r="4.6"/><path d="M6 3.4V6h2"/></svg></div>
  </main>
</div>
</body>
</html>
```